One Pager Marketing Poster for Inspirational Speaker - "Beyond the Horizon Line"

Hi, my name is Dov Hartwell. I'm an inspirational speaker looking to create a marketing one-pager. I used to live with tourettes for 20 years and traveled around the nation talking about compassion and tolerance. My old website is dovhartwell.net. I'm now going out to the corporate market speaking about limiting beliefs and sales.

Front Page: I would love to have half the page with one of the Photos named Photo #1 or Photo #3 that I uploaded and the other half is the following copy:

Beyond The Horizon Line

(then in smaller size below)

Dov Hartwell
Inspirational Sales Speaker

Back Page: I'd like to use the other main photo not used on the front page and the following copy to be on the main page. That would be either photo #1 or #3. I imagine you could use some of the other photos on the page, but if so they should be much smaller.

1. Main Copy
For nearly 20 years Dov Hartwell lived with Tourette’s Syndrome, a disorder deemed by most in the medical community as “involuntary” and “incurable.” It’s estimated he ticced around 25 million times over that time period. He traveled extensively around the nation delivering a message of compassion and tolerance that ultimately earned him national speaking awards at the age of 26. Astonishingly, with the help of top scientific and human potential innovators, Dov completely overcame his Tourette’s in 2010 using only mind-over-body and now lives tic free. Now 30, with his inspiring presentation “Beyond The Horizon Line,” Dov shares his unprecedented story to help companies and sales teams break through the unimaginable.

2: Tagline: Dov’s powerful presentation brings to light what truly holds companies and sales teams back!

3. Value Add:

Bring Dov to your business
• Inspire your sales force
• Understand the role of beliefs
• Gain insights for unbeatable advantages
• Rethink your sales strategy

4. Contact

For additional information contact Ravi
website: beyondthehorizonline.net
email: ravi@dovhartwell.net
phone: (555) –310-4476

5. Logos:
I have been in the Harbor Ledger Daily, on the TV show “Clinic Hour” and have had a QuillTalks talk. I’d like to have these logos on the back page included somehow. (I've attached all the logos)

=========
I added my previous one-pager so you could see the idea behind a one-page. By no means should the new one look like the old one.

Thank you so much for your help.

Target Market(s)

Business in New York City. Sales.

Industry/Entity Type

Marketing

Font styles to use
Sans Serif

Colors
33a6d7
0392cd
3276b5
0455a3
ffffff

Requirements
Must have
• I would really like to use the color scheme blue, black and white. Blue represents trust, dependable and strength and b&w represents balance and calm.

```html
<!DOCTYPE html>
<html lang="en">
<head>
<meta charset="utf-8">
<title>Beyond The Horizon Line – Dov Hartwell</title>
<link href="https://fonts.googleapis.com/css2?family=Open+Sans:ital,wght@0,400;0,600;0,700;0,800;1,400;1,600;1,800&display=swap" rel="stylesheet">
<style>
  :root{
    --sky:#33a6d7;
    --azure:#0392cd;
    --steel:#3276b5;
    --navy:#0455a3;
    --deep:#0a2f5e;
    --white:#ffffff;
    --ink:#2c3440;
    --paper:#eef4fa;
  }
  html,body{margin:0;padding:0;overflow:hidden;}
  body{width:849px;height:1200px;background:var(--paper);font-family:"Open Sans",Arial,sans-serif;color:var(--ink);}
  .poster{position:relative;width:849px;height:1200px;overflow:hidden;background:linear-gradient(180deg,#f6f9fc 0%,#e6eff8 100%);}
  .hero-photo{position:absolute;left:0;top:0;width:849px;height:560px;
    background:radial-gradient(ellipse at 62% 32%,#f2d9a8 0%,#9a7a55 10%,#2c3a52 38%,#12203a 75%,#0a1428 100%);}
  .title-banner{position:absolute;left:250px;top:380px;width:520px;height:230px;}
  .title-banner svg{position:absolute;inset:0;}
  .title-main{position:absolute;left:40px;top:18px;font-style:italic;font-weight:800;font-size:100px;line-height:1;color:var(--navy);letter-spacing:-2px;}
  .title-sub{position:absolute;left:150px;top:136px;font-style:italic;font-weight:600;font-size:46px;line-height:1;color:var(--white);}
  .copy{position:absolute;left:48px;top:622px;width:585px;display:flex;flex-direction:column;gap:14px;}
  .copy p{margin:0;font-size:16.5px;line-height:26px;}
  .story strong{color:var(--navy);font-weight:700;}
  .story-close strong{font-weight:700;}
  .value-box{position:absolute;left:652px;top:565px;width:197px;
    background:linear-gradient(180deg,rgba(51,166,215,.92),rgba(4,85,163,.92));color:var(--white);padding:22px 12px 20px 22px;box-sizing:border-box;}
  .value-box h2{margin:0 0 16px;font-style:italic;font-weight:400;font-size:24px;line-height:29px;}
  .value-box ul{margin:0;padding:0 0 0 16px;font-size:14.5px;font-weight:700;line-height:20px;}
  .value-box li{margin-bottom:6px;}
  .value-box li:last-child{margin-bottom:0;}
  .tagline{position:absolute;left:0;top:972px;width:849px;height:118px;background:linear-gradient(90deg,var(--navy),var(--steel) 60%,var(--azure));
    color:var(--white);font-weight:800;font-size:31px;line-height:40px;display:flex;align-items:center;justify-content:center;text-align:center;margin:0;}
  .contact-band{position:absolute;left:0;top:1090px;width:849px;height:110px;background:linear-gradient(180deg,var(--steel),var(--deep));color:var(--white);}
  .contact-lead{position:absolute;left:48px;top:10px;margin:0;font-style:italic;font-size:20px;line-height:26px;}
  .contact-list{position:absolute;left:48px;top:42px;margin:0;padding:0;list-style:none;font-size:15px;line-height:21px;}
  .contact-list li{display:flex;align-items:center;gap:12px;}
  .contact-list svg{width:16px;height:16px;flex:none;}
  .press{position:absolute;right:34px;top:60px;display:flex;gap:26px;align-items:center;font-weight:700;font-size:15px;}
</style>
</head>
<body>
<div class="poster">
  <div class="hero-photo" role="img" aria-label="Speaker seen from behind on stage facing a large seated audience under warm stage lights"></div>

  <div class="title-banner">
    <svg viewBox="0 0 520 230" width="520" height="230" aria-hidden="true">
      <path d="M18 10 L512 0 L496 222 L0 230 Z" fill="#ffffff" opacity=".96"/>
      <path d="M120 128 L508 122 L500 196 L104 202 Z" fill="#0392cd"/>
    </svg>
    <div class="title-main">Beyond</div>
    <div class="title-sub">The Horizon Line</div>
  </div>

  <div class="copy">
    <p class="story">For nearly 20 years <strong>Dov Hartwell</strong> lived with Tourette’s Syndrome, a disorder deemed by most in the medical community as “involuntary” and “incurable.” <strong>It’s estimated he ticced around 25 million times</strong> over that time period. He traveled extensively around the nation delivering a message of compassion and tolerance that ultimately <strong>earned him national speaking awards</strong> at the age of 26. Astonishingly, with the help of top scientific and human potential innovators, <strong>Dov completely overcame his Tourette’s in 2010</strong> using only mind-over-body and now lives tic free.</p>
    <p class="story-close">Now 30, with his inspiring presentation <strong>“Beyond The Horizon Line,”</strong> Dov shares his unprecedented story to help companies and sales teams break through the unimaginable.</p>
  </div>

  <aside class="value-box">
    <h2>Bring Dov<br>to your business</h2>
    <ul>
      <li>Inspire your sales force</li>
      <li>Understand the role of beliefs</li>
      <li>Gain insights for unbeatable advantages</li>
      <li>Rethink your sales strategy</li>
    </ul>
  </aside>

  <p class="tagline">Dov’s powerful presentation brings to light<br>what truly holds companies and sales teams back!</p>

  <footer class="contact-band">
    <p class="contact-lead">For additional information contact Ravi</p>
    <ul class="contact-list">
      <li><svg viewBox="0 0 18 18"><circle cx="9" cy="9" r="8" fill="none" stroke="#fff" stroke-width="1.6"/><ellipse cx="9" cy="9" rx="3.5" ry="8" fill="none" stroke="#fff" stroke-width="1.2"/><line x1="1" y1="9" x2="17" y2="9" stroke="#fff" stroke-width="1.2"/></svg>beyondthehorizonline.net</li>
      <li><svg viewBox="0 0 18 18"><circle cx="9" cy="9" r="8" fill="none" stroke="#fff" stroke-width="1.6"/><text x="9" y="12.5" text-anchor="middle" font-size="10" font-weight="700" fill="#fff" font-family="Open Sans, sans-serif">@</text></svg>ravi@dovhartwell.net</li>
      <li><svg viewBox="0 0 18 18"><circle cx="9" cy="9" r="8" fill="none" stroke="#fff" stroke-width="1.6"/><path d="M6 5 L7.6 5 L8.4 7.4 L7.4 8.2 Q8.3 10 9.8 10.8 L10.6 9.8 L13 10.6 L13 12.2 Q9 12.6 6 8.6 Q5.6 6.6 6 5 Z" fill="#fff"/></svg>(555) –310-4476</li>
    </ul>
    <div class="press">
      <span>Harbor Ledger Daily</span>
      <span>Clinic Hour</span>
      <span>QuillTalks</span>
    </div>
  </footer>
</div>
</body>
</html>
```